HPS business cards

(Generators . Lighting Towers . De-watering Pumps . Compressors) put under the logo please. my details are Owen Pritchard (Director) 0461527390 harbourpinesupply@postvale.net

```html
<!DOCTYPE html>
<html lang="en">
<head>
<meta charset="utf-8">
<title>HPS Business Cards</title>
<link href="https://fonts.googleapis.com/css2?family=Josefin+Sans:wght@400;600;700&display=swap" rel="stylesheet">
<style>
  :root {
    --stage: #2b2b2d;
    --silver-dark: #8c8d90;
    --silver-mid: #b9babd;
    --silver-light: #eeeff1;
    --silver-ink: #6d6e72;
    --card-white: #ffffff;
    --card-shade: #f1f1f1;
    --gold: #e39a2a;
    --gold-line: #f2d7a8;
    --ink: #3a3a3c;
    --ink-soft: #555558;
  }
  * { margin: 0; padding: 0; box-sizing: border-box; }
  html, body {
    width: 1200px; height: 900px; overflow: hidden;
    background: var(--stage);
    font-family: "Josefin Sans", sans-serif;
  }
  .stage {
    position: relative; width: 1200px; height: 900px;
  }
  .card {
    position: absolute; left: 320px; width: 560px; height: 320px;
    border-radius: 28px;
    box-shadow: 0 14px 30px rgba(0,0,0,.45);
    overflow: hidden;
  }
  .card--front {
    top: 100px;
    background: linear-gradient(100deg,
      var(--silver-dark) 0%, var(--silver-light) 18%, var(--silver-mid) 32%,
      var(--silver-dark) 46%, var(--silver-light) 60%, var(--silver-mid) 74%,
      var(--silver-light) 88%, var(--silver-dark) 100%);
    display: flex; align-items: center; justify-content: center;
  }
  .brand {
    display: flex; align-items: center; gap: 12px;
    font-weight: 700; letter-spacing: .04em; text-transform: uppercase;
  }
  .brand__mark { display: block; width: 22px; height: 22px; }
  .card--front .brand { color: var(--silver-ink); font-size: 34px; }
  .card--front .brand__mark { background: var(--silver-ink); width: 26px; height: 26px; }

  .card--back {
    top: 480px;
    background: linear-gradient(160deg, var(--card-white) 40%, var(--card-shade) 100%);
    text-align: center;
    padding-top: 40px;
  }
  .card--back .brand { justify-content: center; color: var(--gold); font-size: 30px; }
  .card--back .brand__mark { background: var(--gold); }
  .services {
    margin-top: 14px; color: var(--ink); font-size: 17px; line-height: 1.35;
  }
  .services .dot {
    display: inline-block; width: 6px; height: 6px; background: var(--gold);
    margin: 0 6px; vertical-align: middle; position: relative; top: -2px;
  }
  .person {
    margin-top: 22px; display: flex; align-items: center; justify-content: center; gap: 14px;
  }
  .person__rule { width: 110px; height: 1px; background: var(--gold-line); }
  .person__name { color: var(--gold); font-weight: 700; font-size: 24px; }
  .person__role { color: var(--ink-soft); font-size: 17px; margin-top: 2px; }
  .divider { width: 440px; height: 1px; background: var(--gold-line); margin: 18px auto 0; }
  .contact {
    margin-top: 16px; color: var(--ink); font-size: 15px;
    display: flex; align-items: center; justify-content: center; gap: 8px;
  }
  .contact svg { width: 15px; height: 15px; fill: var(--gold); }
  .contact__sep { color: var(--ink-soft); }
</style>
</head>
<body>
<main class="stage">
  <section class="card card--front" aria-label="Card front">
    <div class="brand"><span class="brand__mark"></span>Harbour Pine Supply</div>
  </section>

  <section class="card card--back" aria-label="Card back">
    <div class="brand"><span class="brand__mark"></span>Harbour Pine Supply</div>
    <p class="services">
      Generators<span class="dot"></span>Lighting Towers<br>
      De-watering Pumps<span class="dot"></span>Compressors
    </p>
    <div class="person">
      <span class="person__rule"></span>
      <span class="person__name">Owen Pritchard</span>
      <span class="person__rule"></span>
    </div>
    <p class="person__role">Director</p>
    <div class="divider"></div>
    <p class="contact">
      <svg viewBox="0 0 24 24" aria-hidden="true"><path d="M6.6 10.8a15 15 0 0 0 6.6 6.6l2.2-2.2a1 1 0 0 1 1-.25 11.4 11.4 0 0 0 3.6.57 1 1 0 0 1 1 1V20a1 1 0 0 1-1 1A17 17 0 0 1 3 4a1 1 0 0 1 1-1h3.5a1 1 0 0 1 1 1c0 1.25.2 2.45.57 3.6a1 1 0 0 1-.25 1z"/></svg>
      <span>0461527390</span>
      <span class="contact__sep">|</span>
      <svg viewBox="0 0 24 24" aria-hidden="true"><path d="M2 5h20v14H2zm2 2v.5l8 5 8-5V7zm0 2.8V17h16V9.8l-8 5z"/></svg>
      <span>harbourpinesupply@postvale.net</span>
    </p>
  </section>
</main>
</body>
</html>
```